Speisekarten-Design für italienisches Restaurant im Golfclub mit Blick auf die Alpen
Zielgruppe
Italienisches Restaurant im Golfclub mit Blick auf die Alpen (bei gutem Wetter)
Aufgabenstellung
Karte muss weiterhin bearbeitet werden könne. Es geht um ein Design das optisch anspricht aber nicht übertrieben ist. Die Blätter kommen später in eine Menukarte die noch in Auftrag gegeben werden.
Im Idealfall kann der Designer hierfür auch was mit designen das an einen Firma weitergeben werden kann um die 'Umschläge zu erstellen. Logo kann muss nicht mit drin sein. Es geht auch sehr um die einfache Darstellung des Ganzen.

```html
<!DOCTYPE html>
<html lang="de">
<head>
<meta charset="utf-8">
<title>Ristorante Altamira – Menüs</title>
<link rel="stylesheet" href="https://fonts.googleapis.com/css2?family=Oswald:wght@600&family=Arimo:wght@400&display=swap">
<style>
  :root {
    --paper: #bdb29a;
    --ink: #414043;
    --header: #211f1e;
    --rule: #4a4848;
  }
  * { margin: 0; padding: 0; box-sizing: border-box; }
  html, body { width: 735px; height: 1200px; overflow: hidden; }
  body { background: var(--paper); position: relative; font-family: "Arimo", Arial, sans-serif; color: var(--ink); }

  .masthead {
    position: absolute; left: 0; top: 0; width: 735px; height: 149px;
    background: var(--header);
    display: flex; align-items: center; justify-content: center; gap: 14px;
  }
  .brand-mark { width: 12px; height: 12px; background: var(--paper); }
  .brand-name {
    font-family: "Oswald", "Arial Narrow", sans-serif; font-weight: 600; color: var(--paper);
    font-size: 34px; letter-spacing: 2px; line-height: 1;
  }

  .menu-box, .price-box { position: absolute; border: 1px solid var(--rule); }
  .menu-box { left: 69px; width: 403px; padding: 18px 0 0 16px; }
  .price-box { left: 498px; width: 168px; display: flex; align-items: center; justify-content: center; }
  .menu-title {
    font-family: "Oswald", "Arial Narrow", sans-serif; font-weight: 600;
    font-size: 48px; line-height: 1.05; letter-spacing: -0.5px; margin: 0 0 10px 1px;
  }
  .course-list { list-style: none; font-size: 14px; line-height: 1.15; }
  .course-list li { margin-bottom: 15.3px; }
  .price {
    font-family: "Oswald", "Arial Narrow", sans-serif; font-weight: 600;
    font-size: 48px; margin-left: -34px;
  }

  .menu-1 { top: 177px; height: 240px; }
  .menu-2 { top: 435px; height: 223px; }
  .menu-3 { top: 677px; height: 272px; }
  .menu-3 .menu-title { margin-bottom: 4px; }

  .table-scene {
    position: absolute; left: 213px; top: 996px; width: 311px; height: 170px;
    background: radial-gradient(ellipse at center, #8f8a80 0%, #a8a08e 50%, var(--paper) 75%);
  }
  .footer-bar {
    position: absolute; left: 166px; top: 1170px; width: 402px; height: 30px;
    background: var(--ink);
  }
</style>
</head>
<body>
  <header class="masthead">
    <span class="brand-mark"></span>
    <span class="brand-name">RISTORANTE ALTAMIRA</span>
  </header>

  <section class="menu-box menu-1">
    <h2 class="menu-title">MENU 1</h2>
    <ul class="course-list">
      <li>Appetithäppchen und Aperitif</li>
      <li>Italiensicher Aufschnitt Teller</li>
      <li>Pasta mit Hackfleischsoße und Sahne</li>
      <li>Kalbsbraten mit Barolosoße und Rosmarin Kartoffeln</li>
      <li>Zitronen Sorbet</li>
    </ul>
  </section>
  <div class="price-box menu-1"><span class="price">49,-</span></div>

  <section class="menu-box menu-2">
    <h2 class="menu-title">MENU 2</h2>
    <ul class="course-list">
      <li>Gemischter Salat</li>
      <li>Pasta mit scharfer Tomatensoße</li>
      <li>Putengeschnetzeltes in Currysoße mit Reis</li>
      <li>Tiramisu</li>
    </ul>
  </section>
  <div class="price-box menu-2"><span class="price">35,-</span></div>

  <section class="menu-box menu-3">
    <h2 class="menu-title">MENU 3</h2>
    <ul class="course-list">
      <li>Aperitif</li>
      <li>Vitello Tonnato</li>
      <li>Lasagne im Ofen überbacken</li>
      <li>Rumpsteak tranchiert, auf Rucola Bett serviert mit<br>gehobelten Original Parmesan Käse</li>
      <li>Rosmarinkartoffeln und Gemüse</li>
      <li>Panna Cotta mit Waldfrüchte</li>
    </ul>
  </section>
  <div class="price-box menu-3"><span class="price">55,-</span></div>

  <div class="table-scene" role="img" aria-label="Illustration: gedeckter Bistrotisch mit zwei Weingläsern und zwei Stühlen"></div>
  <div class="footer-bar"></div>
</body>
</html>
```